Business Card Design Project

New Business Card design for Varodine Technology Ltd using new Logo and new Tagline for staffing company.

About us from our website - www.varodine.example:

VaroDine is a leading and recognized Electronic Entertainment, Workforce Augmentation, and Project Management solutions provider with clients in Electronic Entertainment, Legal, Technology, Government and other verticals that range in size from start up organizations to Zenlar 500 companies. VaroDine is certified as an 8(a) minority and woman owned enterprise, established in 1998.

Target Market(s)

Companies in Electronic Entertainment, Legal, Government and Technology

Industry/Entity Type

Business

Requirements
Must have
• Must include in small letters the following information on back:

Established in 1998
8(a)(w)(e), Cage #7KRT9, DUNS #462137580

Front should have the following:
Derek Holloway
Vice President
5820 Birchmont Road
Fallowby, FB 482917
555-318-2746 X 100
555-902-6613 Fax
555-318-2746 Toll Free
name@varodine.example

Our Tagline: Connect • Collaborate • Achieve

```html
<!DOCTYPE html>
<html lang="en">
<head>
<meta charset="utf-8">
<title>VaroDine Business Card</title>
<link href="https://fonts.googleapis.com/css2?family=Montserrat:wght@400;600&family=Cormorant+Garamond:wght@500&display=swap" rel="stylesheet">
<style>
  :root {
    --page: #ffffff;
    --card-grey-top: #d9dadb;
    --card-grey-bottom: #ffffff;
    --contact-blue: #2c62ad;
    --wordmark-grey: #58595b;
    --band-dark: #0c3f6d;
    --band-light: #1b8cc2;
    --band-text: #ffffff;
  }
  * { margin: 0; padding: 0; box-sizing: border-box; }
  html, body {
    width: 1200px; height: 900px; overflow: hidden;
    background: var(--page);
  }
  .canvas { position: relative; width: 1200px; height: 900px; }

  .card { position: absolute; left: 356px; width: 400px; overflow: hidden; }

  /* Front */
  .card-front {
    top: 104px; height: 380px;
    background: linear-gradient(180deg, var(--card-grey-top) 0%, #ececed 55%, var(--card-grey-bottom) 100%);
    font-family: "Montserrat", sans-serif;
    color: var(--contact-blue);
  }
  .person { position: absolute; left: 30px; top: 108px; }
  .person-name { font-size: 22px; font-weight: 400; line-height: 1.1; }
  .person-title { font-size: 13px; margin-top: 3px; }
  .address {
    position: absolute; right: 20px; top: 76px;
    text-align: right; font-size: 12px; line-height: 16px;
  }
  .contact-list {
    position: absolute; right: 20px; top: 128px;
    text-align: right; list-style: none; font-size: 15px; line-height: 32px;
  }
  .wordmark {
    font-family: "Montserrat", sans-serif;
    font-weight: 600;
    color: var(--wordmark-grey);
    letter-spacing: -2px;
    white-space: nowrap;
  }
  .card-front .wordmark {
    position: absolute; left: -4px; top: 262px;
    font-size: 84px; line-height: 1;
  }

  /* Back */
  .card-back {
    top: 500px; height: 344px;
    background: linear-gradient(180deg, var(--card-grey-top) 0%, #f2f2f3 100%);
  }
  .card-back .wordmark {
    position: absolute; left: 0; right: 0; top: 74px;
    text-align: center; font-size: 60px; line-height: 1;
  }
  .back-band {
    position: absolute; left: 0; top: 136px; width: 100%; height: 208px;
    background: linear-gradient(180deg, var(--band-dark) 0%, var(--band-light) 100%);
    color: var(--band-text); text-align: center;
  }
  .tagline, .established {
    font-family: "Cormorant Garamond", serif;
    font-variant: small-caps;
    font-weight: 500;
    font-size: 19px;
    letter-spacing: 0.5px;
  }
  .tagline { margin-top: 76px; }
  .established { margin-top: 16px; }
  .registrations {
    font-family: "Montserrat", sans-serif;
    font-size: 10px; margin-top: 20px;
  }
</style>
</head>
<body>
<main class="canvas">
  <section class="card card-front" aria-label="Business card front">
    <div class="person">
      <p class="person-name">Derek Holloway</p>
      <p class="person-title">Vice President</p>
    </div>
    <address class="address" style="font-style:normal">
      5820 Birchmont Road<br>
      Fallowby, FB 482917
    </address>
    <ul class="contact-list">
      <li>555-318-2746 X 100</li>
      <li>555-902-6613</li>
      <li>1-800-555-0142</li>
      <li>name@varodine.example</li>
    </ul>
    <p class="wordmark">VaroDine</p>
  </section>

  <section class="card card-back" aria-label="Business card back">
    <p class="wordmark">VaroDine</p>
    <div class="back-band">
      <p class="tagline">Connect • Collaborate • Achieve</p>
      <p class="established">Established in 1998</p>
      <p class="registrations">8(a)(w)(e), Cage #7KRT9, DUNS #462137580</p>
    </div>
  </section>
</main>
</body>
</html>
```